Kick-ass motivational company vision poster

We need a company poster that communicates our vision, and keeps us motivated when the going gets tough !

We want a cool graphic design that will stand the test of time, isn't cliched, and is something we're proud to hang around the office.

TEXT
No.1 provider of high quality software development resources in London.

We combine the best of local resourcing with access to a global network, that means we always deliver.

We want our staff to work in jobs they love, and in doing so, deliver fantastic customer service.

SIZE
A1 / A2 portrait

Target Market(s)

employees

Industry/Entity Type

Professional Service

Font styles to use
Sans Serif

Requirements
Must have
• a nice graphic design - appreciate that's pretty broad but we just want a cool design - doesn't necessarily have to match our corporate look and feel (www.qovanltd.com)
Should not have
• Cliche'd use of people / photos / fist punches / clip-art etc. (you get the idea)

```html
<!DOCTYPE html>
<html lang="en">
<head>
<meta charset="utf-8">
<title>Qovan – Company Vision</title>
<link rel="stylesheet" href="https://fonts.googleapis.com/css2?family=Arimo:wght@400;700&display=swap">
<style>
  :root {
    --ink: #0b0b0c;
    --smoke: #6d6e72;
    --smoke-light: #c9cacc;
    --navy: #1f3a8a;
    --navy-deep: #152a6b;
    --paper: #ffffff;
    --orange: #f07a1e;
    --orange-deep: #d9620d;
    --text-navy: #1e3488;
  }
  html, body {
    margin: 0;
    padding: 0;
    overflow: hidden;
    background: var(--ink);
  }
  .poster {
    position: relative;
    width: 849px;
    height: 1200px;
    overflow: hidden;
    background: var(--ink);
    font-family: "Arimo", Arial, sans-serif;
  }
  .backdrop {
    position: absolute;
    inset: 0;
    width: 849px;
    height: 1200px;
  }
  .brand {
    position: absolute;
    left: 42px;
    top: 36px;
    display: flex;
    align-items: center;
    gap: 12px;
    color: var(--paper);
    font-weight: 700;
    font-size: 72px;
    letter-spacing: -2px;
    line-height: 1;
  }
  .brand-dot {
    width: 18px;
    height: 18px;
    border-radius: 50%;
    background: var(--paper);
    margin-top: 14px;
  }
  .statement {
    position: absolute;
    margin: 0;
    font-weight: 400;
    font-size: 27px;
    line-height: 1.3;
  }
  .statement--position {
    left: 320px;
    top: 338px;
    width: 460px;
    color: var(--paper);
  }
  .statement--network {
    left: 40px;
    top: 612px;
    width: 770px;
    text-align: center;
    color: var(--text-navy);
  }
  .statement--people {
    left: 290px;
    top: 918px;
    width: 510px;
    text-align: center;
    color: var(--paper);
  }
</style>
</head>
<body>
<main class="poster">
  <svg class="backdrop" viewBox="0 0 849 1200" role="img" aria-label="Dark background with swirling grey ink smoke and torn paint-brush bands in navy, white and orange">
    <defs>
      <radialGradient id="smoke-top" cx="0.35" cy="0.12" r="0.55">
        <stop offset="0" stop-color="#8a8b8f" stop-opacity="0.75"/>
        <stop offset="1" stop-color="#0b0b0c" stop-opacity="0"/>
      </radialGradient>
      <radialGradient id="smoke-mid" cx="0.15" cy="0.7" r="0.45">
        <stop offset="0" stop-color="#9a9b9e" stop-opacity="0.6"/>
        <stop offset="1" stop-color="#0b0b0c" stop-opacity="0"/>
      </radialGradient>
      <radialGradient id="smoke-low" cx="0.85" cy="0.95" r="0.4">
        <stop offset="0" stop-color="#7c7d80" stop-opacity="0.6"/>
        <stop offset="1" stop-color="#0b0b0c" stop-opacity="0"/>
      </radialGradient>
      <linearGradient id="band-navy" x1="0" y1="0" x2="1" y2="0">
        <stop offset="0" stop-color="#152a6b"/>
        <stop offset="0.5" stop-color="#1f3a8a"/>
        <stop offset="1" stop-color="#223f94"/>
      </linearGradient>
      <linearGradient id="band-white" x1="0" y1="0" x2="0" y2="1">
        <stop offset="0" stop-color="#e9eaeb"/>
        <stop offset="0.25" stop-color="#ffffff"/>
        <stop offset="1" stop-color="#f4f4f4"/>
      </linearGradient>
      <linearGradient id="band-orange" x1="0" y1="0" x2="1" y2="0">
        <stop offset="0" stop-color="#d9620d"/>
        <stop offset="0.4" stop-color="#f07a1e"/>
        <stop offset="1" stop-color="#f58a2a"/>
      </linearGradient>
    </defs>

    <rect width="849" height="1200" fill="#0b0b0c"/>
    <rect width="849" height="1200" fill="url(#smoke-top)"/>
    <rect width="849" height="1200" fill="url(#smoke-mid)"/>
    <rect width="849" height="1200" fill="url(#smoke-low)"/>

    <!-- top-right orange flare -->
    <path d="M560 0 H849 V130 C800 150 760 110 720 120 C680 130 640 90 610 60 C590 40 570 20 560 0 Z" fill="url(#band-orange)" opacity="0.9"/>

    <!-- navy band -->
    <path d="M0 300 C80 280 160 300 240 282 C360 262 480 290 600 270 C700 256 790 280 849 266 V470 C760 480 680 458 600 476 C480 496 360 468 240 482 C150 492 70 470 0 484 Z" fill="url(#band-navy)"/>

    <!-- orange strip beneath navy band -->
    <path d="M0 482 C120 470 260 492 400 478 C520 466 600 488 700 476 V500 C600 512 500 494 380 506 C250 518 120 498 0 510 Z" fill="#c85a12" opacity="0.85"/>

    <!-- white band -->
    <path d="M0 520 C120 500 250 530 380 508 C520 486 660 520 849 500 V790 C740 806 620 780 500 798 C360 818 220 786 100 804 C60 810 30 800 0 806 Z" fill="url(#band-white)"/>

    <!-- orange band -->
    <path d="M200 860 C320 840 460 866 600 846 C700 834 780 850 849 840 V1110 C760 1122 660 1100 560 1114 C440 1130 320 1104 220 1116 C180 1060 160 990 170 930 C176 900 186 876 200 860 Z" fill="url(#band-orange)"/>
  </svg>

  <div class="brand">
    <span class="brand-name">qovan</span>
    <span class="brand-dot"></span>
  </div>

  <p class="statement statement--position">No.1 provider of high quality software development resources in London.</p>

  <p class="statement statement--network">We combine the best of local resourcing<br>with access to a global network,<br>that means we always deliver.</p>

  <p class="statement statement--people">We want our staff to work<br>in jobs they love, and in doing so,<br>deliver fantastic customer service.</p>
</main>
</body>
</html>
```